Harbor Vitality Chocolate Shake Label

We need a new label design for our Harbor Vitality Chocolate Protein Shake. The design needs to include all the composition info as per the attached Trim Meadow Chocolate shake label with a fresh new eye catching design that will stand out on retail store shelves. It must include our Harbor Vitality Logo and portray a professional image that inspires trust. It must indicate that it is a chocolate shake that looks tasty and inviting. Harbor Vitality is a product sold by healthcare practitioners.

Industry/Entity Type

Health And Wellness

Requirements
Must have
• The Harbor Vitality logo. Contain all the attached info as per the chocolate Trim Meadow label. Feature something that indicates it is a chocolate shake on the label that looks tasty and inviting.
Nice to have
• I have attached some of the other products in our range. Would be a bonus if it can match into the existing look and feel somehow.

```html
<!DOCTYPE html>
<html lang="en">
<head>
<meta charset="utf-8">
<title>Harbor Vitality Chocolate Protein Shake Label</title>
<link href="https://fonts.googleapis.com/css2?family=Arimo:wght@400;700&family=Chewy&family=Oswald:wght@300;400&display=swap" rel="stylesheet">
<style>
  :root{
    --blue:#1ea4d8;
    --blue-dark:#1589bd;
    --navy:#1f3a5a;
    --cocoa:#3a2014;
    --ink:#222;
    --grey:#666;
    --page:#ffffff;
  }
  *{margin:0;padding:0;box-sizing:border-box}
  html,body{width:1066px;height:1200px;overflow:hidden;background:var(--page)}
  body{font-family:"Arimo",sans-serif;color:var(--ink);position:relative}
  .label{position:absolute;left:18px;top:451px;width:1030px;height:297px;background:#fff;box-shadow:0 2px 6px rgba(0,0,0,.18);overflow:hidden}
  .abs{position:absolute}

  /* nutrition panel */
  .panel-title{font-weight:700;color:var(--blue);font-size:7px}
  .small{font-size:4.6px;line-height:6.2px}
  .nutrition-title{left:19px;top:10px}
  .serving-notes{left:19px;top:20px;width:300px}
  .col-head{top:46px;height:12px;border-top:1.5px solid var(--blue);border-bottom:1.5px solid var(--blue);font-size:6.4px;font-weight:700;color:var(--blue);display:flex;align-items:center}
  .head-left{left:19px;width:142px;justify-content:center}
  .head-right{left:164px;width:142px;padding-left:8px}
  .col-divider{left:161px;top:46px;width:1.5px;height:130px;background:var(--blue)}
  .facts{font-size:4.6px;line-height:8.2px}
  .facts li{list-style:none;display:flex;justify-content:space-between}
  .facts-left{left:19px;top:63px;width:136px}
  .facts-right{left:171px;top:63px;width:129px}
  .right-rule{left:164px;top:176px;width:142px;height:1.5px;background:var(--blue)}
  .ingredients-title{left:171px;top:180px;font-size:6px}
  .ingredients{left:171px;top:190px;width:148px}
  .allergens{left:19px;top:242px;width:146px;color:var(--blue);font-weight:700;font-size:4.4px;line-height:5.8px}

  /* centre front panel */
  .flavour-tab{left:499px;top:0;width:195px;height:15px;background:var(--blue);color:#fff;font-size:12px;display:flex;align-items:center;justify-content:center}
  .brand{left:363px;top:22px;display:flex;align-items:center;gap:6px}
  .brand-dot{width:26px;height:26px;border-radius:50%;background:var(--blue)}
  .brand-name{font-size:18px;font-weight:700;color:var(--navy)}
  .flavour-banner{left:350px;top:75px;width:210px;height:52px;background:linear-gradient(90deg,var(--blue),var(--blue-dark));border-radius:0 14px 0 0;display:flex;align-items:center;justify-content:center;overflow:hidden}
  .flavour-word{font-family:"Chewy",sans-serif;font-size:42px;color:var(--cocoa);letter-spacing:.5px;line-height:1;white-space:nowrap}
  .product-name{left:358px;top:132px;width:200px;font-family:"Oswald",sans-serif;font-weight:300;font-size:31px;color:var(--navy);letter-spacing:.5px;line-height:1;white-space:nowrap;overflow:hidden}
  .stats{left:358px;top:183px;display:flex;align-items:flex-start;gap:4px;color:var(--navy)}
  .stat{text-align:center;font-size:14px;line-height:1}
  .stat span{display:block;font-size:5.8px;color:var(--grey);margin-top:3px}
  .slash{width:12px;height:34px}
  .chocolate-visual{left:574px;top:120px;width:120px;height:90px;border-radius:6px;background:linear-gradient(135deg,#8a5a3a,#5a3320 55%,#c2a284)}
  .free-from{left:350px;top:241px;width:330px;text-align:center;font-size:9.5px;line-height:12px}
  .footer-band{left:0;top:268px;width:1030px;height:29px;background:linear-gradient(180deg,var(--blue),var(--blue-dark));color:#fff;display:flex;align-items:center;justify-content:center;gap:8px}
  .footer-band strong{font-size:13px;font-weight:400;letter-spacing:.3px}
  .footer-band em{font-style:normal;font-size:9.5px}

  /* info panel */
  .info{left:755px;top:8px;width:195px;text-align:center;font-size:6.3px;line-height:8.4px}
  .info h3{font-size:7.6px;color:var(--blue);margin-bottom:1px}
  .info .block{padding:3px 0 4px;border-bottom:1.5px solid var(--blue)}
  .info .plain{border:none}
  .info .caps{font-weight:700;font-size:5.8px;line-height:8px}
  .info .caps-light{font-size:5.8px;line-height:8px}
  .info .blue{color:var(--blue);font-weight:700}
  .reg{left:880px;top:252px;font-size:7.6px;font-weight:700}
</style>
</head>
<body>
<main class="label">
  <!-- nutrition panel -->
  <h2 class="abs panel-title nutrition-title">NUTRITION FACTS:</h2>
  <p class="abs small serving-notes">Servings Size 50ml (2×25ml level scoopfulsy).<br>Servings per 500g containers: +28 days<br>Suggestions for use: Blender or shake 50ml with 250ml water or slim milk.</p>
  <div class="abs col-head head-left">Amount pr serving of 30g</div>
  <div class="abs col-head head-right">Vitamin Blend Based on 30% of RDA</div>
  <div class="abs col-divider"></div>
  <ul class="abs facts facts-left">
    <li><span>Protein</span><span>7 g</span></li>
    <li><span>Carbohydrate</span><span>16 g</span></li>
    <li><span>Fiber</span><span>2.5 g</span></li>
    <li><span>Fat</span><span>1 g</span></li>
    <li><span>Energy</span><span>438 kj</span></li>
    <li><span>Sodium</span><span>106 mg</span></li>
    <li><span>Potassium</span><span>156 mg</span></li>
    <li><span>Calcium</span><span>203 mg</span></li>
    <li><span>Magnesium</span><span>48 mg</span></li>
    <li><span>Phosphorous</span><span>174 mg</span></li>
    <li><span>L-Glutamine</span><span>100 mg</span></li>
    <li><span>Garcinia Cambogia Extract</span><span>37.5 mg</span></li>
    <li><span>Chlorine</span><span>30 mg</span></li>
    <li><span>Pyruvite</span><span>21.8 mg</span></li>
    <li><span>L-Carnitine</span><span>15 mg</span></li>
    <li><span>Zinc</span><span>4.5 mg</span></li>
    <li><span>Molybdenum</span><span>28.5 mg</span></li>
    <li><span>Selenium</span><span>15 mcg</span></li>
    <li><span>Chromium Picolinate</span><span>10.8 mcg</span></li>
  </ul>
  <ul class="abs facts facts-right">
    <li><span>Vitamin C</span><span>18 mg</span></li>
    <li><span>Nicotinamide</span><span>5.4 mg</span></li>
    <li><span>Pantothenic Acid</span><span>1.8 mg</span></li>
    <li><span>Vitamin B2</span><span>480 mcg</span></li>
    <li><span>Vitamin B6</span><span>600 mcg</span></li>
    <li><span>Vitamin B1</span><span>420 mcg</span></li>
    <li><span>Vitamine A</span><span>300 RE</span></li>
    <li><span>Follic Acid</span><span>80 mcg</span></li>
    <li><span>Biotin</span><span>24 mcg</span></li>
    <li><span>Vitamin E</span><span>3 TE</span></li>
    <li><span>Vitamin D</span><span>1.5 mcg</span></li>
    <li><span>Vitamin B12</span><span>0.3 mcg</span></li>
  </ul>
  <div class="abs right-rule"></div>
  <h3 class="abs panel-title ingredients-title">INGREDIENTS:</h3>
  <p class="abs small ingredients">Skim Milk powder, Fructose, Maltodextrin, Soy protein isolate, Fructooligosacharides, Whey protein concentrate, Calcium caseinate, Instant starch, MCT oil, Flavourants, Calcium phosphate, Stabilizers, l-glutamine, Calcium pyruvate, Selenium, a.a.c salt, Potassium phosphate, Magnesium oxide,Vitamin premix, Garcinia cambogia extract, Choline bitartrate, Inositol, Zinc lactate, l-carnitine, Molybdenum a.a.c, Sucralose sweetener blend, colourants, Manganese lactate, Chromium Picolinate.</p>
  <p class="abs allergens">ALLERGENS: MADE IN A FACTORY THAT PROCESSES COW'S MILK, EGG, SOY, GLUTEN (WHEAT, BARLEY AND OATS), FISH, TREE NUTS AND PEANUTS.</p>

  <!-- front panel -->
  <div class="abs flavour-tab">Chocolate Flavour Shake</div>
  <div class="abs brand"><span class="brand-dot"></span><span class="brand-name">Harbor Vitality</span></div>
  <div class="abs flavour-banner"><span class="flavour-word">Chocolate</span></div>
  <h1 class="abs product-name">PROTEIN SHAKE</h1>
  <div class="abs stats">
    <div class="stat">00G<span>PROTEIN</span></div>
    <svg class="slash" viewBox="0 0 12 34"><line x1="10" y1="1" x2="2" y2="33" stroke="#1f3a5a" stroke-width="1.6"/></svg>
    <div class="stat">00G<span>CARBS</span></div>
    <svg class="slash" viewBox="0 0 12 34"><line x1="10" y1="1" x2="2" y2="33" stroke="#1f3a5a" stroke-width="1.6"/></svg>
    <div class="stat">000<span>KCALS</span></div>
    <svg class="slash" viewBox="0 0 12 34"><line x1="10" y1="1" x2="2" y2="33" stroke="#1f3a5a" stroke-width="1.6"/></svg>
    <div class="stat">00MG<span>PER<br>SERVING</span></div>
  </div>
  <div class="abs chocolate-visual" role="img" aria-label="Photo of chocolate pieces with shavings and a mint leaf"></div>
  <p class="abs free-from">FREE from trans fats, socrose, aspartame, effedra, caffine,<br>artificial stimulants, wheat, gluten, yeast, corn, and preservatives.</p>

  <!-- info panel -->
  <section class="abs info">
    <div class="block">
      <h3>CONTAINER INFO:</h3>
      Servings per containers: +28 days<br>Servings size: +50ml<br>• Protein Blend Shake is a dietary supplement.
    </div>
    <div class="block">
      <h3>SUGGESTED USE:</h3>
      As a dietary supplement, use to replace one protein meal per day. Blend two 25ml level scoopfuls with a full glass of water or skim milk in a shaker/blender.
    </div>
    <div class="block">
      <h3>KEEP OUT OF REACH OF CHILDREN:</h3>
      <span class="caps-light">STORE IN A COOL DRY PLACE. DO NOT USE IF THE TAMPER EVIDENT SEAL IS MISSING OR BROKEN.</span>
    </div>
    <div class="block plain">
      <p class="caps">CONSULT WITH YOUR PHYSICIAN BEFORE USING THIS PRODUCT IF YOU ARE PREGNANT, LACTATING OR SUSPECT YOU MAY BE SENSITIVE TO ANY OF THE INGREDIENTS.</p>
      <p style="margin-top:6px;font-weight:700">Manufactured In South Africa</p>
      <p class="blue" style="margin-top:2px">Distributed By:</p>
      <p>Trim Meadow Medical Weight Loss(Pty)Ltd.</p>
      <p>Pretoria. South Africa</p>
      <p class="blue">Customer Service:</p>
      <p>086 01 2457</p>
      <p class="blue">www.trimmeadow.co.za</p>
    </div>
  </section>
  <p class="abs reg">MCC Reg. Appl. No. :004218</p>

  <div class="abs footer-band"><strong>DIETARY SUPPLEMENT</strong><em>NETWT (450 G)</em></div>
</main>
</body>
</html>
```